Rollo's Ground Prep & Grading

I would like to have business cards created for my land clearing company. We have excavators, skid steers, dump trucks, tractor trailer dump trailers, forestry mulchers along with all size tractors for pasture restoration and arena builds.

Target Market(s)

Both commercial and residential clients

Contact Information for Business Card

Name, phone number, email and website

Colors

Designer to choose colors to be used in the design.

```html
<!DOCTYPE html>
<html lang="en">
<head>
<meta charset="utf-8">
<title>Rollo's Ground Prep &amp; Grading – Business Card</title>
<link rel="stylesheet" href="https://fonts.googleapis.com/css2?family=Roboto+Condensed:wght@400;700&family=Montserrat:wght@500;600&display=swap">
<style>
  :root {
    --page-bg: #e9e7e6;
    --card-black: #050505;
    --accent-yellow: #f5c211;
    --band-orange: #e36a26;
    --text-white: #ffffff;
    --sky-blue: #3b86b8;
    --sky-glow: #f29a2e;
    --earth-brown: #7a5a3c;
    --machine-yellow: #d9a524;
  }
  * { margin: 0; padding: 0; box-sizing: border-box; }
  html, body {
    width: 1200px; height: 991px; overflow: hidden;
    background: var(--page-bg);
  }
  .business-card {
    position: absolute; left: 75px; top: 195px;
    width: 1050px; height: 600px;
    background: var(--card-black);
    overflow: hidden;
    box-shadow: 0 10px 30px rgba(0,0,0,.25);
    font-family: "Montserrat", sans-serif;
    color: var(--text-white);
  }
  .site-photo {
    position: absolute; left: 420px; top: 0; width: 630px; height: 600px;
    background:
      linear-gradient(180deg, var(--sky-blue) 0%, var(--sky-glow) 38%, var(--machine-yellow) 58%, var(--earth-brown) 78%, #4a3322 100%);
  }
  .photo-fade {
    position: absolute; left: 420px; top: 0; width: 360px; height: 600px;
    background: linear-gradient(90deg, var(--card-black) 0%, rgba(5,5,5,.85) 45%, rgba(5,5,5,0) 100%);
  }
  .brand {
    position: absolute; left: 60px; top: 42px;
    display: flex; align-items: center; gap: 22px;
  }
  .brand-name {
    font-family: "Roboto Condensed", sans-serif; font-weight: 700;
    font-size: 46px; line-height: 1; color: var(--text-white);
  }
  .brand-mark {
    width: 78px; height: 78px; border-radius: 50%;
    background: var(--accent-yellow);
  }
  .title-rule {
    position: absolute; left: 0; top: 140px; width: 640px; height: 3px;
    background: linear-gradient(90deg, var(--accent-yellow) 70%, rgba(245,194,17,0));
  }
  .service-list {
    position: absolute; list-style: none;
    font-size: 17px; font-weight: 500; line-height: 26px;
  }
  .service-list li::before { content: "* "; }
  .services-primary { left: 60px; top: 168px; }
  .services-secondary { left: 420px; top: 168px; }
  .contact-band {
    position: absolute; left: 0; top: 420px; width: 620px; height: 180px;
    background: linear-gradient(90deg, var(--band-orange) 75%, rgba(227,106,38,0));
    border-top: 4px solid var(--accent-yellow);
    padding: 26px 0 0 60px;
  }
  .contact-phone {
    font-family: "Roboto Condensed", sans-serif; font-weight: 700;
    font-size: 44px; line-height: 1.1;
  }
  .contact-line { font-size: 19px; font-weight: 600; margin-top: 8px; }
</style>
</head>
<body>
  <div class="business-card">
    <div class="site-photo" role="img" aria-label="Excavator digging soil under a sunset sky with blue and orange clouds"></div>
    <div class="photo-fade"></div>

    <div class="brand">
      <h1 class="brand-name">Rollo's Ground Prep &amp; Grading</h1>
      <span class="brand-mark"></span>
    </div>
    <div class="title-rule"></div>

    <ul class="service-list services-primary">
      <li>Excavation Services</li>
      <li>Site Clearing</li>
      <li>Land Clearing</li>
      <li>Demolition Services</li>
      <li>Bobcat Services</li>
      <li>Shoring</li>
      <li>Land Demolition</li>
      <li>Grading Service</li>
      <li>Regrading</li>
    </ul>
    <ul class="service-list services-secondary">
      <li>Resloping</li>
      <li>Site Preparation</li>
      <li>Building Site Preparation</li>
      <li>Land Site Preparation</li>
      <li>Construction Demolition</li>
      <li>Forestry Mulching</li>
      <li>Pasture Reseeding</li>
      <li>Build Arenas</li>
      <li>Pasture Stump Removal</li>
    </ul>

    <div class="contact-band">
      <p class="contact-phone">(555) 014-2290</p>
      <p class="contact-line">info@rollosgroundprep.com</p>
      <p class="contact-line">www.rollosgroundprep.com</p>
    </div>
  </div>
</body>
</html>
```